The Plaster & Resonance Craftworks Inc (PRCI)

Create a LOGO and Business Card design.

Colors: Black, Bright Yellow & Red

Description of company: commercial carpentry, metal framing, drywall, taping/spackling, demolition, rough/finish carpentry.

Target Market(s)

developers, architects, general contractors, construction managers

Industry/Entity Type

Business

```html
<!DOCTYPE html>
<html lang="en">
<head>
<meta charset="utf-8">
<title>P.R.C.I Business Card</title>
<link href="https://fonts.googleapis.com/css2?family=Saira+Condensed:wght@400;500&display=swap" rel="stylesheet">
<style>
  :root {
    --page-bg: #1b1b1b;
    --card-bg: #000000;
    --brand-yellow: #ffee00;
    --brand-red: #e0100f;
    --rule-red: #8a1414;
  }
  * { margin: 0; padding: 0; box-sizing: border-box; }
  html, body {
    width: 927px;
    height: 1200px;
    overflow: hidden;
    background: var(--page-bg);
    font-family: "Saira Condensed", "Arial Narrow", sans-serif;
  }
  .canvas { position: relative; width: 927px; height: 1200px; }
  .card {
    position: absolute;
    background: var(--card-bg);
    text-align: center;
  }
  .card--front { left: 141px; top: 135px; width: 659px; height: 385px; }
  .card--back { left: 147px; top: 560px; width: 660px; height: 384px; }

  .brand-name {
    position: absolute;
    left: 0; right: 0;
    top: 78px;
    color: var(--brand-yellow);
    font-size: 190px;
    font-weight: 500;
    line-height: 1;
    letter-spacing: 6px;
  }
  .brand-rule {
    position: absolute;
    left: 104px;
    width: 465px;
    top: 302px;
    height: 1px;
    background: var(--rule-red);
  }
  .tagline {
    position: absolute;
    left: 0; right: 0;
    top: 311px;
    color: var(--brand-yellow);
    font-size: 31px;
    font-weight: 400;
    line-height: 1.2;
  }

  .brand-name--small {
    position: absolute;
    left: 0; right: 0;
    top: 50px;
    color: var(--brand-yellow);
    font-size: 48px;
    font-weight: 500;
    line-height: 1;
    letter-spacing: 2px;
  }
  .contact {
    position: absolute;
    left: 0; right: 0;
    color: var(--brand-red);
    font-size: 32px;
    font-weight: 400;
    line-height: 40px;
  }
  .contact--address { top: 132px; }
  .contact--phone { top: 172px; }
  .contact--web { top: 276px; }
</style>
</head>
<body>
<main class="canvas">
  <section class="card card--front">
    <div class="brand-name">P.R.C.I</div>
    <div class="brand-rule"></div>
    <p class="tagline">The Plaster &amp; Resonance Craftworks Inc</p>
  </section>

  <section class="card card--back">
    <div class="brand-name--small">P.R.C.I</div>
    <p class="contact contact--address">2270 Ember Lane/Fairhaven Ohio/45099</p>
    <p class="contact contact--phone">Call us: (555)214-8830</p>
    <p class="contact contact--web">Visit us online at: prci-build.com</p>
  </section>
</main>
</body>
</html>
```